3" Round Business Card for Funeral Home

We need a business card designed for our cremation service. We would like to use a 3" round business card.

The business card will be 2-sided. One side with the logo featured prominently. The back sad will have employee name and contact info.

Templates for printing have been attached to project as well as logo

We like soft colors like the logo. Final design should promote a feeling of trust.

Industry/Entity Type

Funeral

Contact Information for Business Card

Employee Name, Phone number, email, web address

Requirements
Should not have
• any sort of funeral item such as urn, casket, hearse, tombstone

```html
<!DOCTYPE html>
<html lang="en">
<head>
<meta charset="utf-8">
<title>EmberRest.com – Round Business Card</title>
<link rel="stylesheet" href="https://fonts.googleapis.com/css2?family=Poppins:wght@300;400;600&display=swap">
<style>
  :root {
    --teal: #1aaba1;
    --purple: #8e2a91;
    --white: #ffffff;
    --backdrop: #efe7da;
    --shadow: rgba(60, 40, 20, 0.28);
  }
  * { margin: 0; padding: 0; box-sizing: border-box; }
  html, body {
    width: 1200px; height: 900px; overflow: hidden;
    background: var(--backdrop);
    font-family: "Poppins", sans-serif;
  }
  .stage { position: relative; width: 1200px; height: 900px; }
  .card {
    position: absolute;
    top: 282px;
    width: 374px; height: 374px;
    border-radius: 50%;
    overflow: hidden;
    box-shadow: 6px 8px 14px var(--shadow);
  }
  .card--front { left: 191px; background: var(--white); }
  .card--back { left: 634px; background: var(--teal); }
  .card svg { display: block; width: 374px; height: 374px; }
  .brand-name { font-weight: 400; letter-spacing: -0.5px; }
  .brand-name--teal { fill: var(--teal); }
  .brand-name--white { fill: var(--white); }
  .employee-line {
    fill: var(--purple); font-weight: 600; font-size: 16px; letter-spacing: 1.4px;
  }
  .contact-text { fill: var(--white); font-weight: 300; font-size: 13.5px; }
  .icon-badge { fill: var(--purple); }
  .icon-glyph { fill: none; stroke: var(--white); stroke-width: 1.1; stroke-linecap: round; stroke-linejoin: round; }
</style>
</head>
<body>
<main class="stage">

  <section class="card card--front" aria-label="Card front with contact details">
    <svg viewBox="0 0 374 374" xmlns="http://www.w3.org/2000/svg">
      <defs>
        <path id="name-curve" d="M52 194 C 120 186, 180 150, 230 134 S 300 118, 316 116"/>
      </defs>

      <text class="brand-name brand-name--teal" x="187" y="84" font-size="28" text-anchor="middle">emberrest.com</text>

      <!-- purple wave band -->
      <path fill="var(--purple)" d="M0 183 C 30 200, 55 208, 85 207 C 160 205, 220 140, 289 138 C 330 137, 360 140, 374 141 L 374 177 C 350 162, 320 155, 289 156 C 220 158, 160 210, 85 211 C 55 212, 25 202, 0 192 Z"/>
      <!-- teal lower section with white separator -->
      <path fill="var(--teal)" d="M0 197 C 25 207, 55 216, 85 215 C 160 214, 220 162, 289 160 C 320 159, 350 167, 374 182 L 374 374 L 0 374 Z"/>

      <text class="employee-line"><textPath href="#name-curve">DANA ELLISON | DIRECTOR</textPath></text>

      <text class="contact-text" text-anchor="middle">
        <tspan x="187" y="231">210 E Harbor Lane,</tspan>
        <tspan x="187" y="248">Suite B2 Mesa, AZ 85201</tspan>
      </text>

      <g class="contact-icons">
        <circle class="icon-badge" cx="167" cy="264" r="7"/>
        <path class="icon-glyph" d="M164.5 260.5 c -0.5 2.5 2 6 5 7 l1.2 -1.4 -1.8 -1.2 -0.9 0.8 c -1 -0.5 -2 -1.6 -2.3 -2.5 l0.8 -0.9 -1.1 -1.9 z"/>
        <circle class="icon-badge" cx="187" cy="264" r="7"/>
        <rect class="icon-glyph" x="183.3" y="261.5" width="7.4" height="5" rx="0.6"/>
        <path class="icon-glyph" d="M183.5 262 l3.5 2.6 3.5 -2.6"/>
        <circle class="icon-badge" cx="207" cy="264" r="7"/>
        <circle class="icon-glyph" cx="207" cy="264" r="4"/>
        <path class="icon-glyph" d="M203 264 h8 M207 260 c -2 2.5 -2 5.5 0 8 M207 260 c 2 2.5 2 5.5 0 8"/>
      </g>

      <text class="contact-text" text-anchor="middle">
        <tspan x="187" y="290">480-555-0132</tspan>
        <tspan x="187" y="307">info@emberrest.com</tspan>
        <tspan x="187" y="323">www.emberrest.com</tspan>
      </text>
    </svg>
  </section>

  <section class="card card--back" aria-label="Card back with brand name">
    <svg viewBox="0 0 374 374" xmlns="http://www.w3.org/2000/svg">
      <text class="brand-name brand-name--white" x="187" y="196" font-size="38" text-anchor="middle">emberrest.com</text>
    </svg>
  </section>

</main>
</body>
</html>
```